New web design for a service provider in the medical field

We are looking for a new design for our website. We are a company that repairs and sells medical endoscopes. Our customers include doctors and hospitals. Our current website can be found at https://lumenfix.example/en/lumenfix-english.
We need a new web design (without programming) for the following 3 pages:
-Startpage https://lumenfix.example/en/lumenfix-english/
-Used endoscopes https://lumenfix.example/en/used-endoscopes/
-Purchase https://lumenfix.example/en/purchase/
The design should be modern and stylish.
The blue color of the logo should be reflected on the page, but not too intrusive.
I have uploaded the images from the header. If more images are needed, let me know and I will upload them.

Target Market(s)
Doctors and hospitals

```html
<!DOCTYPE html>
<html lang="en">
<head>
<meta charset="utf-8">
<title>LumenFix – Endoscope Repair</title>
<link href="https://fonts.googleapis.com/css2?family=Manrope:wght@400;500;600;700&display=swap" rel="stylesheet">
<style>
:root{
  --blue:#1a9fdd;
  --blue-light:#e6f4fb;
  --navy:#132447;
  --ink:#1f2a44;
  --muted:#5c6478;
  --line:#d9dee6;
  --star:#f5a30b;
  --white:#ffffff;
}
*{box-sizing:border-box;margin:0;padding:0}
html,body{width:1200px;height:2989px;overflow:hidden}
body{position:relative;font-family:"Manrope",sans-serif;color:var(--ink);background:var(--white)}
.abs{position:absolute}
a{color:inherit;text-decoration:none}

/* hero */
.hero-bg{left:0;top:0;width:1200px;height:680px;background:linear-gradient(180deg,#f4fafe 0%,#e4f2fb 100%)}
.hero-photo{left:700px;top:140px;width:500px;height:450px;background:linear-gradient(135deg,#c9d3dc 0%,#7d8894 55%,#4a535e 100%)}
.hero-wave{left:0;top:540px;width:1200px;height:150px}
.logo{display:flex;align-items:center;gap:10px;font-weight:700;font-size:21px;color:var(--navy)}
.logo .dot{width:14px;height:14px;border-radius:50%;background:var(--blue)}
.site-logo{left:86px;top:52px}
.nav{left:430px;top:54px;display:flex;gap:31px;font-size:17px;font-weight:500;align-items:center}
.nav .caret{display:inline-block;width:8px;height:8px;border-right:2px solid var(--ink);border-bottom:2px solid var(--ink);transform:rotate(45deg);margin-left:8px;position:relative;top:-3px}
.nav-icons{left:1048px;top:50px;display:flex;gap:10px}
.nav-icons span{width:30px;height:30px;border-radius:50%;background:var(--navy);display:flex;align-items:center;justify-content:center}
.nav-rule{left:416px;top:102px;width:701px;height:2px;background:var(--line)}
.hero-title{left:148px;top:186px;font-size:42px;line-height:49px;font-weight:600;color:var(--navy)}
.hero-text{left:148px;top:355px;width:505px;font-size:17px;line-height:23px;color:var(--muted)}
.btn{display:flex;align-items:center;justify-content:center;gap:8px;background:var(--blue);color:var(--white);font-weight:600;font-size:17px;border-radius:4px}
.hero-btn{left:148px;top:453px;width:155px;height:60px}

/* intro */
.intro-title{left:133px;top:716px;font-size:30px;line-height:36px;font-weight:600;color:var(--navy)}
.intro-title em{font-style:normal;color:var(--blue)}
.intro-text{left:571px;top:718px;width:490px;font-size:17px;line-height:22.5px;color:var(--muted)}
.card{width:256px;height:154px;border:2px solid var(--line);border-radius:10px;display:flex;flex-direction:column;align-items:center;justify-content:center;gap:16px;font-size:20px;font-weight:600;color:var(--navy);background:var(--white)}
.card.active{border-color:var(--blue)}

/* pickup */
.pickup-photo{left:84px;top:1173px;width:506px;height:286px}
.pickup-title{left:635px;top:1182px;font-size:30px;line-height:36px;font-weight:600;color:var(--navy)}
.pickup-text{left:637px;top:1270px;width:395px;font-size:17px;line-height:22.5px;color:var(--muted)}
.pickup-btn{left:637px;top:1388px;width:155px;height:60px}

/* features */
.band{left:0;top:1588px;width:1200px;height:1030px;background:var(--blue-light)}
.panel{left:82px;top:1535px;width:1035px;height:658px;background:var(--white);border:2px solid var(--line);border-radius:24px}
.feat-heading{left:0;top:1568px;width:1200px;text-align:center;font-size:30px;font-weight:600;color:var(--navy)}
.feat-intro{left:290px;top:1616px;width:620px;text-align:center;font-size:17px;line-height:22.5px;color:var(--muted)}
.feat{display:flex;gap:26px;width:480px}
.feat .ico{flex:0 0 72px;height:72px;border-radius:50%;border:2px solid var(--line);display:flex;align-items:center;justify-content:center;margin-top:10px}
.feat h3{font-size:20px;font-weight:600;color:var(--navy);margin-bottom:8px}
.feat p{font-size:17px;line-height:22.5px;color:var(--muted);max-width:375px}

/* testimonials */
.test-heading{left:0;top:2245px;width:1200px;text-align:center;font-size:30px;font-weight:600;color:var(--navy)}
.review{width:330px;height:236px;background:var(--white);border-radius:12px;box-shadow:0 6px 20px rgba(19,36,71,.08);padding:18px 19px}
.review .top{display:flex;justify-content:space-between;align-items:flex-start}
.avatar{width:48px;height:48px;background:linear-gradient(135deg,#e9b64a,#c98a2f)}
.avatar.b{background:linear-gradient(135deg,#cfe6ef,#8fb8c8)}
.avatar.c{background:linear-gradient(135deg,#f0c23d,#d49520)}
.stars{display:flex;gap:9px;margin-top:4px}
.review h4{font-size:20px;font-weight:600;color:var(--navy);margin:20px 0 12px}
.review p{font-size:17px;line-height:22.5px;color:var(--muted);max-width:292px}
.arrow{width:42px;height:42px;border-radius:50%;background:var(--white);display:flex;align-items:center;justify-content:center;box-shadow:0 2px 8px rgba(0,0,0,.06)}

/* footer */
.footer{left:0;top:2610px;width:1200px;height:379px;background:var(--navy);color:var(--white)}
.footer .logo{color:var(--white);position:absolute;left:100px;top:92px;font-size:22px}
.foot-text{left:87px;top:165px;width:290px;font-size:17px;line-height:22.5px;color:#c3cad8}
.foot-col{font-size:17px}
.foot-col h5{font-size:20px;font-weight:600;color:var(--blue);margin-bottom:14px}
.foot-col li{list-style:none;margin-bottom:14px}
.news-text{left:850px;top:100px;width:265px;font-size:17px;line-height:22.5px}
.news-input{left:844px;top:173px;width:273px;height:48px;border-radius:24px;background:#1c3158;color:#7f8aa3;font-size:16px;display:flex;align-items:center;justify-content:center}
.news-btn{left:844px;top:230px;width:273px;height:48px;border-radius:24px}
.copy{left:82px;top:346px;font-size:16px;color:#9aa3b7}
.social{left:982px;top:346px;display:flex;gap:18px}
.social span{width:20px;height:20px;border-radius:50%;border:1.6px solid #9aa3b7}
</style>
</head>
<body>

<div class="abs hero-bg"></div>
<div class="abs hero-photo" role="img" aria-label="Photo of a flexible endoscope control head"></div>
<svg class="abs hero-wave" viewBox="0 0 1200 150" preserveAspectRatio="none"><path d="M0 120 C200 40 380 60 560 95 C760 135 950 60 1200 10 L1200 150 L0 150 Z" fill="#ffffff"/></svg>

<header>
  <a class="abs logo site-logo" href="https://lumenfix.example/en/lumenfix-english/"><span class="dot"></span>LumenFix</a>
  <nav class="abs nav">
    <a href="https://lumenfix.example/en/lumenfix-english/">Endoscope Repair</a>
    <a href="https://lumenfix.example/en/used-endoscopes/">Used Endoscopes<span class="caret"></span></a>
    <a href="#">Accessories<span class="caret"></span></a>
    <a href="https://lumenfix.example/en/purchase/">Purchase</a>
  </nav>
  <div class="abs nav-icons">
    <span><svg width="14" height="14" viewBox="0 0 24 24" fill="none" stroke="#fff" stroke-width="2"><path d="M5 3h4l2 5-3 2a12 12 0 0 0 6 6l2-3 5 2v4a2 2 0 0 1-2 2A17 17 0 0 1 3 5a2 2 0 0 1 2-2z"/></svg></span>
    <span><svg width="14" height="14" viewBox="0 0 24 24" fill="none" stroke="#fff" stroke-width="2"><rect x="3" y="5" width="18" height="14" rx="2"/><path d="M3 7l9 6 9-6"/></svg></span>
  </div>
  <div class="abs nav-rule"></div>
</header>

<section>
  <h1 class="abs hero-title">Put your Endoscope<br>in reliable hands<br>with LumenFix!</h1>
  <p class="abs hero-text">We are specialised in the repair and sale of Orvale, Pentrix and Fujora flexible medical endoscopes. As a service-oriented company, we are at your side with our knowledge and skills!</p>
  <a class="abs btn hero-btn" href="#">Get Started
    <svg width="14" height="14" viewBox="0 0 24 24" fill="none" stroke="#fff" stroke-width="2.4"><path d="M6 6l12 12M18 8v10H8"/></svg></a>
</section>

<section>
  <h2 class="abs intro-title">Endoscope repairs and<br>second hand endoscopes<br>from <em>LumenFix</em> – cause<br>the outcome matters!</h2>
  <p class="abs intro-text">LumenFix is a privileged partner for the start-up facility or optimisation of existing healthcare facilities, doctor's offices and hospitals. The quality and reliability of our products and our offered service are our best advertisement!<br>As a result of optimised processes and highly qualified specialists in our company, we can work very quickly and with high quality for your benefit of least possible restrictions in your doctor's office or in your hospital.</p>

  <div class="abs card" style="left:197px;top:950px">
    <svg width="48" height="48" viewBox="0 0 48 48" fill="none" stroke="#132447" stroke-width="2.2"><path d="M8 8l14 14M6 12l6-6M26 26l14 14-4 4-14-14M30 6a8 8 0 0 0 10 10l-24 24-6 2 2-6z"/></svg>
    Repair Endoscope</div>
  <div class="abs card" style="left:472px;top:950px">
    <svg width="50" height="48" viewBox="0 0 50 48" fill="none" stroke="#132447" stroke-width="2.2"><rect x="4" y="18" width="42" height="22" rx="2"/><path d="M12 18V8h26v10M20 4h10"/><text x="25" y="34" text-anchor="middle" font-size="12" font-family="Manrope,sans-serif" font-weight="700" fill="#132447" stroke="none">SELL</text></svg>
    Sell Endoscope</div>
  <div class="abs card active" style="left:746px;top:950px">
    <svg width="50" height="48" viewBox="0 0 50 48" fill="none" stroke="#132447" stroke-width="2.2"><path d="M25 18L8 12l17-6 17 6zM8 12v20l17 8 17-8V12M25 18v22M4 20l21 8 21-8"/></svg>
    Purchase Endoscope</div>
</section>

<section>
  <svg class="abs pickup-photo" viewBox="0 0 506 286" role="img" aria-label="Photo of an endoscope mounted on a holder">
    <defs><linearGradient id="pg" x1="0" y1="0" x2="1" y2="1"><stop offset="0" stop-color="#e8eaed"/><stop offset=".5" stop-color="#8c9096"/><stop offset="1" stop-color="#d6d8db"/></linearGradient></defs>
    <path d="M470 0 L506 0 L506 286 L490 286 Z" fill="#d6ecf8"/>
    <path d="M0 0 L470 0 L492 286 L18 286 Z" fill="url(#pg)"/>
  </svg>
  <h2 class="abs pickup-title">Our Pick-up service can<br>take care of it!</h2>
  <p class="abs pickup-text">Faulty or Defective endoscope? We ensure quick and smooth repairs! We want to help you so that there are least possible restrictions in your doctor's office or hospital!</p>
  <a class="abs btn pickup-btn" href="#">Pick-Up Order</a>
</section>

<section>
  <div class="abs band"></div>
  <div class="abs panel"></div>
  <h2 class="abs feat-heading">Cause the outcome matters!</h2>
  <p class="abs feat-intro">Lorem ipsum dolor sit amet, consectetur adipiscing elit. Auctor habitasse aliquet congue nisl cursus at. Tempor varius convallis mauris at nec massa suscipit cursus porttitor. Adipiscing sit volutpat vitae vitae non posuere diam.</p>

  <div class="abs feat" style="left:121px;top:1725px">
    <div class="ico"><svg width="36" height="36" viewBox="0 0 36 36" fill="none" stroke="#1a9fdd" stroke-width="1.8"><circle cx="20" cy="20" r="11"/><path d="M20 14v6l4 3M17 5h6M20 5v4M3 18h5M4 23h5"/></svg></div>
    <div><h3>Fast repairs</h3><p>Keep potential disruptions in your doctor's office or in your hospital at minimum as a result of optimized processes and highly qualified specialists in our company</p></div>
  </div>
  <div class="abs feat" style="left:605px;top:1725px">
    <div class="ico"><svg width="36" height="36" viewBox="0 0 36 36" fill="none" stroke="#1a9fdd" stroke-width="1.8"><circle cx="20" cy="13" r="8"/><path d="M20 9v8M17 11h5M17 15h5M4 26l6-4h8l-2 4h-6M16 26l10-5 3 2-12 8H4"/></svg></div>
    <div><h3>Highly cost efficient</h3><p>Benefit from our first class recommendations and implementation by our experienced staff. Our goals is to find the best solutions together with you at the best lowest price point</p></div>
  </div>
  <div class="abs feat" style="left:121px;top:1888px">
    <div class="ico"><svg width="36" height="36" viewBox="0 0 36 36" fill="none" stroke="#1a9fdd" stroke-width="1.8"><path d="M4 16L18 5l14 11M8 13v18h20V13"/><rect x="13" y="18" width="10" height="10"/><path d="M18 18v10M13 23h10"/></svg></div>
    <div><h3>On-site service</h3><p>We will gladly pay you a visit to to carry out analysis and repairs on site. Due to our many years of experience – it doesn't get any faster (whigleithin a 250 km range)</p></div>
  </div>
  <div class="abs feat" style="left:605px;top:1888px">
    <div class="ico"><svg width="36" height="36" viewBox="0 0 36 36" fill="none" stroke="#1a9fdd" stroke-width="1.8"><rect x="8" y="5" width="22" height="26" rx="2"/><circle cx="15" cy="20" r="5"/><path d="M21 12h6M21 17h6M21 22h6M21 27h6M12 10h4"/></svg></div>
    <div><h3>Loan equipment service</h3><p>Use our service of high-quality loan devices during the downtime of your defective endoscope (limited to stock)</p></div>
  </div>
  <div class="abs feat" style="left:121px;top:2051px">
    <div class="ico"><svg width="36" height="36" viewBox="0 0 36 36" fill="none" stroke="#1a9fdd" stroke-width="1.8"><path d="M14 6l10 10M24 6l-10 10M12 4l4 4M26 4l-4 4M4 24l6-3h8l-2 4h-6M16 25l10-5 3 2-12 8H4"/></svg></div>
    <div><h3>Without a maintenance contract</h3><p>No subscription or other maintenance contract, but one-time and sustainable repair work</p></div>
  </div>
  <div class="abs feat" style="left:605px;top:2051px">
    <div class="ico"><svg width="36" height="36" viewBox="0 0 36 36" fill="none" stroke="#1a9fdd" stroke-width="1.8"><circle cx="18" cy="16" r="10"/><path d="M18 10l2 4 4 .5-3 3 1 4-4-2-4 2 1-4-3-3 4-.5zM12 24l-3 8 5-2 3 3 1-7M24 24l3 8-5-2-3 3"/></svg></div>
    <div style="padding-top:10px"><h3>First class service</h3><p>Our clients always come first!</p></div>
  </div>
</section>

<section>
  <h2 class="abs test-heading">Let's see what our clients say</h2>
  <div class="abs arrow" style="left:26px;top:2407px"><svg width="20" height="20" viewBox="0 0 24 24" fill="none" stroke="#1a9fdd" stroke-width="2.2"><path d="M20 12H5M11 6l-6 6 6 6"/></svg></div>
  <div class="abs arrow" style="left:1131px;top:2407px"><svg width="20" height="20" viewBox="0 0 24 24" fill="none" stroke="#1a9fdd" stroke-width="2.2"><path d="M4 12h15M13 6l6 6-6 6"/></svg></div>

  <article class="abs review" style="left:84px;top:2310px">
    <div class="top"><div class="avatar" role="img" aria-label="Client portrait"></div>
      <div class="stars">
        <svg width="22" height="22" viewBox="0 0 24 24"><path d="M12 2l3 7 7 .6-5.4 4.7 1.7 7.2L12 17.8 5.7 21.5l1.7-7.2L2 9.6 9 9z" fill="#f5a30b"/></svg>
        <svg width="22" height="22" viewBox="0 0 24 24"><path d="M12 2l3 7 7 .6-5.4 4.7 1.7 7.2L12 17.8 5.7 21.5l1.7-7.2L2 9.6 9 9z" fill="#f5a30b"/></svg>
        <svg width="22" height="22" viewBox="0 0 24 24"><path d="M12 2l3 7 7 .6-5.4 4.7 1.7 7.2L12 17.8 5.7 21.5l1.7-7.2L2 9.6 9 9z" fill="#f5a30b"/></svg>
        <svg width="22" height="22" viewBox="0 0 24 24"><path d="M12 2l3 7 7 .6-5.4 4.7 1.7 7.2L12 17.8 5.7 21.5l1.7-7.2L2 9.6 9 9z" fill="none" stroke="#f5a30b" stroke-width="1.6"/><path d="M12 2v15.8L5.7 21.5l1.7-7.2L2 9.6 9 9z" fill="#f5a30b"/></svg>
        <svg width="22" height="22" viewBox="0 0 24 24"><path d="M12 2l3 7 7 .6-5.4 4.7 1.7 7.2L12 17.8 5.7 21.5l1.7-7.2L2 9.6 9 9z" fill="none" stroke="#f5a30b" stroke-width="1.6"/></svg>
      </div></div>
    <h4>Dana Whitfield</h4>
    <p>Amet minim mollit non deserunt ullamco est sit aliqua dolor do amet sint. Velit officia consequat duis enim velit mollit....</p>
  </article>

  <article class="abs review" style="left:435px;top:2310px">
    <div class="top"><div class="avatar b" role="img" aria-label="Client portrait"></div>
      <div class="stars">
        <svg width="22" height="22" viewBox="0 0 24 24"><path d="M12 2l3 7 7 .6-5.4 4.7 1.7 7.2L12 17.8 5.7 21.5l1.7-7.2L2 9.6 9 9z" fill="#f5a30b"/></svg>
        <svg width="22" height="22" viewBox="0 0 24 24"><path d="M12 2l3 7 7 .6-5.4 4.7 1.7 7.2L12 17.8 5.7 21.5l1.7-7.2L2 9.6 9 9z" fill="#f5a30b"/></svg>
        <svg width="22" height="22" viewBox="0 0 24 24"><path d="M12 2l3 7 7 .6-5.4 4.7 1.7 7.2L12 17.8 5.7 21.5l1.7-7.2L2 9.6 9 9z" fill="#f5a30b"/></svg>
        <svg width="22" height="22" viewBox="0 0 24 24"><path d="M12 2l3 7 7 .6-5.4 4.7 1.7 7.2L12 17.8 5.7 21.5l1.7-7.2L2 9.6 9 9z" fill="#f5a30b"/></svg>
        <svg width="22" height="22" viewBox="0 0 24 24"><path d="M12 2l3 7 7 .6-5.4 4.7 1.7 7.2L12 17.8 5.7 21.5l1.7-7.2L2 9.6 9 9z" fill="none" stroke="#f5a30b" stroke-width="1.6"/></svg>
      </div></div>
    <h4>Marcus Ellery</h4>
    <p>ullamco est sit aliqua dolor do amet sint. Velit officia consequat duis enim velit mollit. Exercitation veniam consequat sunt nostrud amet.</p>
  </article>

  <article class="abs review" style="left:786px;top:2310px">
    <div class="top"><div class="avatar c" role="img" aria-label="Client portrait"></div>
      <div class="stars">
        <svg width="22" height="22" viewBox="0 0 24 24"><path d="M12 2l3 7 7 .6-5.4 4.7 1.7 7.2L12 17.8 5.7 21.5l1.7-7.2L2 9.6 9 9z" fill="#f5a30b"/></svg>
        <svg width="22" height="22" viewBox="0 0 24 24"><path d="M12 2l3 7 7 .6-5.4 4.7 1.7 7.2L12 17.8 5.7 21.5l1.7-7.2L2 9.6 9 9z" fill="#f5a30b"/></svg>
        <svg width="22" height="22" viewBox="0 0 24 24"><path d="M12 2l3 7 7 .6-5.4 4.7 1.7 7.2L12 17.8 5.7 21.5l1.7-7.2L2 9.6 9 9z" fill="#f5a30b"/></svg>
        <svg width="22" height="22" viewBox="0 0 24 24"><path d="M12 2l3 7 7 .6-5.4 4.7 1.7 7.2L12 17.8 5.7 21.5l1.7-7.2L2 9.6 9 9z" fill="none" stroke="#f5a30b" stroke-width="1.6"/><path d="M12 2v15.8L5.7 21.5l1.7-7.2L2 9.6 9 9z" fill="#f5a30b"/></svg>
        <svg width="22" height="22" viewBox="0 0 24 24"><path d="M12 2l3 7 7 .6-5.4 4.7 1.7 7.2L12 17.8 5.7 21.5l1.7-7.2L2 9.6 9 9z" fill="none" stroke="#f5a30b" stroke-width="1.6"/></svg>
      </div></div>
    <h4>Priya Halden</h4>
    <p>Amet minim mollit non deserunt ullamco est sit aliqua dolor do amet sint. Velit officia consequat duis enim velit mollit....</p>
  </article>
</section>

<footer class="abs footer">
  <div class="logo"><span class="dot"></span>LumenFix</div>
  <p class="abs foot-text">Lorem ipsum dolor sit amet, consectetur adipiscing elit, sed do eiusmod tempor incididunt ut labore et dolore magna aliqua. Ut enim ad minim veniam</p>
  <div class="abs foot-col" style="left:461px;top:60px">
    <h5>LumenFix</h5>
    <ul><li>Endoscope Repair</li><li>Used Endoscopes</li><li>Accessories</li><li>Purchase</li></ul>
  </div>
  <div class="abs foot-col" style="left:659px;top:60px">
    <h5>About</h5>
    <ul><li>Support</li><li>Contact</li><li>Terms</li><li>Blog</li></ul>
  </div>
  <div class="abs foot-col" style="left:850px;top:60px"><h5>Subscribe to our Newsletter</h5></div>
  <p class="abs news-text">Lorem ipsum dolor sit amet, consectetur adipiscing elit, sed do eiusmod</p>
  <div class="abs news-input">Enter email address</div>
  <a class="abs btn news-btn" href="#">Submit
    <svg width="18" height="18" viewBox="0 0 24 24" fill="none" stroke="#fff" stroke-width="2.2"><path d="M4 12h15M13 6l6 6-6 6"/></svg></a>
  <p class="abs copy">Copyright © 2022</p>
  <div class="abs social"><span></span><span></span><span></span><span></span></div>
</footer>

</body>
</html>
```